Looking for a modern, Professional business card design

We have a simple business card, but are looking for a more modern, professional look. A sample of the basic card is attached as well as the logo. We would also like to add that we offer:
Struggling with your finances?
- Learn to become debt free
- Discover the power of cash
- Control your money instead of it controlling you
Let us help you achieve a new level of financial freedom!
Also, we would like to have a "SPECIAL OFFER!: FREE 30 minute consultation"
Financial Planning

```html
<!DOCTYPE html>
<html lang="en">
<head>
<meta charset="utf-8">
<title>Steady Ledger Coaching – Business Cards</title>
<link rel="stylesheet" href="https://fonts.googleapis.com/css2?family=Quicksand:wght@500;600;700&family=Russo+One&display=swap">
<style>
:root{
  --stage:#2b2b2b;
  --card:#ffffff;
  --ink:#111111;
  --green:#7cc52b;
  --green-deep:#4f9a1c;
  --band:#0b0b0b;
}
*{box-sizing:border-box;margin:0;padding:0}
html,body{width:1200px;height:900px;overflow:hidden;background:var(--stage)}
.canvas{position:relative;width:1200px;height:900px}
.card{position:absolute;width:700px;height:400px;background:var(--card);border-radius:22px;overflow:hidden;font-family:"Quicksand",sans-serif;color:var(--ink)}
.card-back{left:60px;top:50px;text-align:center}
.card-front{left:440px;top:470px}

.brand{display:flex;align-items:center;gap:12px;font-family:"Quicksand",sans-serif;font-weight:700;color:var(--ink);font-size:30px;letter-spacing:.5px}
.brand-dot{width:22px;height:22px;border-radius:50%;background:var(--green);flex:none}
.card-back .brand{justify-content:center;margin-top:52px}

.site{font-size:19px;font-weight:600;margin-top:16px}
.accent{color:var(--green)}
.pill{display:inline-block;margin-top:12px;padding:4px 18px;border:2.5px solid var(--ink);border-radius:30px;font-size:20px;font-weight:700;letter-spacing:.5px}
.benefits{list-style:none;margin-top:14px;font-size:20px;font-weight:600;line-height:1.5}
.benefits .accent{font-weight:700}

.band{position:absolute;left:0;top:0;width:700px;height:400px}
.corner-mark{position:absolute;right:0;top:26px;width:22px;height:40px;background:var(--green)}
.person{position:absolute;right:38px;top:32px;text-align:right}
.person-name{font-family:"Russo One",sans-serif;font-size:26px;color:var(--green);letter-spacing:1px}
.person-role{font-family:"Russo One",sans-serif;font-size:13px;letter-spacing:1px;margin-top:2px}
.card-front .brand{position:absolute;left:40px;top:112px;font-size:28px}
.offer{position:absolute;left:40px;top:168px;font-size:20px;font-weight:600}
.offer .tag{font-family:"Russo One",sans-serif;color:var(--green);font-size:17px;letter-spacing:.5px}
.offer .free{font-family:"Russo One",sans-serif;font-size:17px}
.offer .green{color:var(--green)}
.contact{position:absolute;left:40px;top:260px;list-style:none;color:#fff;font-size:19px;font-weight:600;line-height:1.6}
.contact li{display:flex;align-items:center;gap:12px}
.contact svg{width:16px;height:16px;flex:none}
</style>
</head>
<body>
<main class="canvas">

  <section class="card card-back">
    <div class="brand"><span class="brand-dot"></span>Steady Ledger Coaching</div>
    <p class="site">www.<span class="accent">steadyledgercoaching</span>.com</p>
    <p class="pill"><span class="accent">STRUGGLING</span> WITH YOUR <span class="accent">FINANCES?</span></p>
    <ul class="benefits">
      <li>Learn to become debt free</li>
      <li>Discover the power of cash</li>
      <li>Control your money instead of it controlling you</li>
      <li>Let us help you achieve a new level of financial <span class="accent">FREEDOM!</span></li>
    </ul>
  </section>

  <section class="card card-front">
    <svg class="band" viewBox="0 0 700 400" aria-hidden="true">
      <path d="M0 235 L440 235 Q560 235 620 300 L700 380 L700 400 L0 400 Z" fill="var(--band)"/>
    </svg>
    <span class="corner-mark"></span>
    <div class="person">
      <p class="person-name">DANIEL R. HAYES</p>
      <p class="person-role">PERSONAL FINANCIAL COACH</p>
    </div>
    <div class="brand"><span class="brand-dot"></span>Steady Ledger Coaching</div>
    <p class="offer"><span class="tag">SPECIAL OFFER!</span> <span class="free">FREE</span> 30 <span class="green">minute consultation</span></p>
    <ul class="contact">
      <li><svg viewBox="0 0 16 16"><rect x="4" y="1" width="8" height="14" rx="1.5" fill="none" stroke="var(--green)" stroke-width="1.6"/><circle cx="8" cy="12.3" r="0.9" fill="var(--green)"/></svg>(205) 555-0148</li>
      <li><svg viewBox="0 0 16 16"><rect x="1" y="3.5" width="14" height="9" fill="none" stroke="var(--green)" stroke-width="1.6"/><path d="M1 3.5 L8 9 L15 3.5" fill="none" stroke="var(--green)" stroke-width="1.6"/></svg>daniel@steadyledgercoaching.com</li>
      <li><svg viewBox="0 0 16 16"><circle cx="8" cy="8" r="6.5" fill="none" stroke="var(--green)" stroke-width="1.5"/><ellipse cx="8" cy="8" rx="2.8" ry="6.5" fill="none" stroke="var(--green)" stroke-width="1.2"/><path d="M1.5 8 H14.5" stroke="var(--green)" stroke-width="1.2"/></svg>www.<span class="accent">steadyledgercoaching</span>.com</li>
    </ul>
  </section>

</main>
</body>
</html>
```